Velmora Facebook Ads Design (examples provided)

We provide Google Data Studio, Google Sheets and Microsoft Excel Connectors and templates. https://chartspan.quorvel.com/
Our core audience is Digital marketing agencies, but anyone who owns a business and uses any of these ad platforms https://velmora-frontend.brixwelldev.tech/product-data-connector can use our connectors and reports.
I am looking to have high converting Facebook ad & Google Display images made. Our website is here (in progress) the domain is Velmora.ai
Tagline -
Smart Reporting, Made Simple
Few Features we have -
Free Forever Plan
Free High-end Templates
Popular data studio connectors -
https://velmora-frontend.brixwelldev.tech/product-data-connector
I would like the designs to have black background and be VIBRANT, visuals that will stop users from scrolling on Facebook.
Nice designs but please - I have attached 4 concepts that I would like each designer to COPY but use my site's color scheme and swap out the people with new versions, putting your own spin on the designs. These are the highest converting SaaS designs of 2023, so I know they work, I just need versions for my brand.
Here are specific details https://files.paperlune.net/document/d/7Qa-kp2LMT_wXyRbTn4ZsFhUeVoCjKdPq8mAgHiYr3Lb/edit?usp=sharing
Digital marketing's agencies or anyone with a business' that uses Google data studio

```html
<!DOCTYPE html>
<html lang="en">
<head>
<meta charset="utf-8">
<title>Velmora.ai – Smart Reporting Made Simple</title>
<link rel="stylesheet" href="https://fonts.googleapis.com/css2?family=Montserrat:wght@400;500;600;700;800&family=Roboto:wght@400;500;700;900&display=swap">
<style>
  :root {
    --page: #1b2747;
    --card-shadow: #16224a;
    --bar-blue: #4a64b0;
    --card: #ffffff;
    --divider: #c5d4f0;
    --navy: #1d2b4f;
    --icon: #2c3e6e;
    --icon-blue: #3f5fb5;
    --soft-blue: #7b9be0;
    --avatar: #a9bfe9;
    --alert: #f0304a;
    --like-blue: #1a6ed8;
    --ink: #0b0b0d;
    --white: #ffffff;
    --bg-light: #e6e6e7;
    --bg-mid: #d2d2d4;
    --tab-dark: #232325;
    --blue: #4f7df0;
    --violet: #8f6fd2;
    --pink: #e0409f;
    --magenta: #e255c9;
  }
  * { margin: 0; padding: 0; box-sizing: border-box; }
  html, body {
    width: 1200px; height: 1200px; overflow: hidden;
    background: var(--page);
  }
  .stage {
    position: relative;
    width: 1932px; height: 1932px;
    transform: scale(0.621118);
    transform-origin: 0 0;
    background: var(--page);
    font-family: "Roboto", sans-serif;
  }
  .post-shadow {
    position: absolute; left: 478px; top: 154px;
    width: 974px; height: 1662px;
    background: var(--card-shadow);
  }
  .post {
    position: absolute; left: 458px; top: 134px;
    width: 974px; height: 1662px;
    background: var(--card);
    overflow: hidden;
  }
  .top-bar { position: absolute; left: 0; top: 0; width: 100%; height: 41px; background: var(--bar-blue); }
  .nav-icons { position: absolute; left: 0; top: 0; }
  .nav-rule { position: absolute; left: 0; top: 170px; width: 100%; height: 3px; background: var(--divider); }

  .author {
    position: absolute; left: 149px; top: 225px;
    font-size: 40px; font-weight: 700; color: var(--navy); line-height: 1;
  }
  .time {
    position: absolute; left: 150px; top: 269px;
    font-size: 34px; font-weight: 400; color: var(--soft-blue); line-height: 1;
  }
  .description {
    position: absolute; left: 35px; top: 357px;
    font-size: 32px; font-weight: 400; color: var(--navy); line-height: 1;
  }
  .description .tag { color: var(--soft-blue); }

  .reaction-count {
    position: absolute; left: 144px; top: 1453px;
    font-size: 36px; color: var(--navy); line-height: 1;
  }
  .share-count {
    position: absolute; right: 4px; top: 1453px;
    font-size: 36px; color: var(--navy); line-height: 1;
  }
  .action-rule { position: absolute; left: 0; top: 1528px; width: 100%; height: 3px; background: var(--divider); }
  .action {
    position: absolute; top: 1578px;
    font-size: 40px; color: var(--soft-blue); line-height: 1;
  }
  .action.like { left: 240px; }
  .action.share { left: 732px; }

  /* ad creative */
  .ad {
    position: absolute; left: 0; top: 434px;
    width: 975px; height: 976px;
    overflow: hidden;
    background: radial-gradient(ellipse at 70% 45%, #efefef 0%, var(--bg-light) 45%, var(--bg-mid) 100%);
    font-family: "Montserrat", sans-serif;
  }
  .brand-tab {
    position: absolute; right: 0; top: 0;
    width: 350px; height: 132px;
    background: var(--tab-dark);
    border-bottom-left-radius: 52px;
    display: flex; align-items: center; gap: 18px;
    padding-left: 30px;
  }
  .brand-dot { width: 30px; height: 30px; border-radius: 50%; background: var(--blue); flex: none; }
  .brand-name { color: var(--white); font-weight: 400; font-size: 46px; letter-spacing: -0.5px; white-space: nowrap; }
  .photo {
    position: absolute; left: 345px; top: 160px;
    width: 630px; height: 816px;
    background: linear-gradient(160deg, #d9d9db 0%, #bdbdc0 30%, #3a3a3e 65%, #1e1e22 100%);
    clip-path: polygon(62% 0, 100% 0, 100% 100%, 38% 100%, 0 72%, 10% 50%, 40% 35%, 55% 10%);
  }
  .headline { color: var(--ink); line-height: 1; }
  .headline span { position: absolute; left: 42px; white-space: nowrap; }
  .headline .line-1 { top: 61px; font-size: 92px; font-weight: 400; }
  .headline .line-2 { top: 175px; font-size: 88px; font-weight: 800; }
  .headline .line-3 {
    top: 277px; font-size: 90px; font-weight: 800;
    background: linear-gradient(90deg, var(--blue) 0%, var(--violet) 35%, var(--pink) 60%, var(--magenta) 100%);
    -webkit-background-clip: text; background-clip: text; color: transparent;
  }
  .feature-panel {
    position: absolute; left: 0; top: 440px;
    width: 660px; height: 536px;
    background: linear-gradient(135deg, var(--blue) 0%, var(--violet) 45%, var(--pink) 100%);
    clip-path: polygon(0 0, 46% 0, 100% 100%, 0 100%);
  }
  .features { font-family: "Roboto", sans-serif; line-height: 1; color: var(--white); }
  .features span { position: absolute; left: 44px; white-space: nowrap; }
  .features .few { top: 460px; font-size: 58px; font-weight: 400; }
  .features .title { top: 520px; font-size: 58px; font-weight: 700; }
  .features .we-have { top: 586px; font-size: 74px; font-weight: 900; color: var(--ink); }
  .features .rule { top: 669px; left: 42px; width: 170px; height: 6px; background: var(--ink); }
  .feature-list {
    position: absolute; left: 44px; top: 697px;
    list-style: none; color: var(--white);
    font-size: 27px; font-weight: 500; line-height: 42px;
  }
  .feature-list li { height: 42px; line-height: 1; }
  .cta {
    position: absolute; left: 42px; top: 785px;
    width: 147px; height: 48px;
    border: 2px solid var(--ink); border-radius: 8px;
    background: linear-gradient(90deg, #3fb4f2 0%, var(--violet) 50%, var(--magenta) 100%);
    display: flex; align-items: center; justify-content: center; gap: 6px;
    font-family: "Roboto", sans-serif; font-weight: 700; font-size: 18px; color: var(--ink);
  }
  .socials { position: absolute; left: 43px; top: 862px; display: flex; gap: 22px; }
  .socials span { width: 50px; height: 50px; border-radius: 50%; background: var(--ink); }
  .site-url {
    position: absolute; left: 44px; top: 925px;
    color: var(--white); font-size: 15px; font-weight: 600; line-height: 1; white-space: nowrap;
  }
</style>
</head>
<body>
<div class="stage">
  <div class="post-shadow"></div>
  <article class="post">
    <div class="top-bar"></div>

    <svg class="nav-icons" width="974" height="170" viewBox="0 0 974 170" aria-hidden="true">
      <g fill="none" stroke-width="4" stroke-linecap="round" stroke-linejoin="round">
        <rect x="35" y="76" width="60" height="58" rx="8" stroke="var(--icon-blue)"/>
        <path d="M35 98 H95 V84 a8 8 0 0 0 -8 -8 H43 a8 8 0 0 0 -8 8 Z" fill="var(--icon-blue)" stroke="var(--icon-blue)"/>
        <circle cx="49" cy="88" r="4" fill="#fff" stroke="none"/>
        <line x1="60" y1="88" x2="84" y2="88" stroke="#fff"/>

        <g stroke="var(--icon)">
          <circle cx="292" cy="98" r="14"/>
          <path d="M272 131 v-6 a20 20 0 0 1 40 0 v6 Z"/>
          <circle cx="324" cy="102" r="12"/>
          <path d="M316 131 h25 v-5 a17 17 0 0 0 -22 -16"/>
        </g>
        <circle cx="337" cy="88" r="10" fill="var(--alert)" stroke="none"/>

        <g stroke="var(--icon)">
          <rect x="484" y="80" width="48" height="50" rx="4"/>
          <line x1="484" y1="94" x2="532" y2="94"/>
          <path d="M484 94 q6 10 12 0 q6 10 12 0 q6 10 12 0 q6 10 12 0"/>
          <rect x="498" y="110" width="20" height="20"/>
        </g>

        <g stroke="var(--icon)">
          <path d="M700 124 q8 -6 8 -18 v-8 a16 16 0 0 1 32 0 v8 q0 12 8 18 Z"/>
          <circle cx="724" cy="78" r="4"/>
          <path d="M718 128 a6 6 0 0 0 12 0"/>
        </g>
        <circle cx="750" cy="88" r="10" fill="var(--alert)" stroke="none"/>

        <g stroke="var(--icon)">
          <line x1="876" y1="88" x2="920" y2="88"/>
          <line x1="876" y1="107" x2="930" y2="107"/>
          <line x1="876" y1="126" x2="930" y2="126"/>
        </g>
        <circle cx="928" cy="86" r="8" fill="var(--icon-blue)" stroke="none"/>
      </g>
      <g>
        <circle cx="81" cy="262" r="46" fill="var(--avatar)"/>
        <circle cx="81" cy="260" r="19" fill="#fff"/>
        <path d="M46 292 a40 30 0 0 1 70 0 a46 46 0 0 1 -70 0 Z" fill="#fff"/>
        <circle cx="929" cy="266" r="5" fill="var(--soft-blue)"/>
        <circle cx="946" cy="266" r="5" fill="var(--soft-blue)"/>
        <circle cx="963" cy="266" r="5" fill="var(--soft-blue)"/>
      </g>
    </svg>

    <div class="nav-rule"></div>

    <p class="author">Your text here</p>
    <p class="time">10:30 AM</p>
    <p class="description">Your description here <span class="tag">#hashtag</span></p>

    <section class="ad">
      <div class="photo" role="img" aria-label="Photo of a smiling man in glasses and a dark suit pointing at the features list"></div>

      <h1 class="headline">
        <span class="line-1">Smart</span>
        <span class="line-2">Reporting</span>
        <span class="line-3">Made Simple</span>
      </h1>

      <div class="brand-tab">
        <span class="brand-dot"></span>
        <span class="brand-name">Velmora.ai</span>
      </div>

      <div class="feature-panel"></div>

      <h2 class="features">
        <span class="few">Few</span>
        <span class="title">Features</span>
        <span class="we-have">We Have</span>
        <span class="rule"></span>
      </h2>

      <ul class="feature-list">
        <li>Free Forever Plan</li>
        <li>Free High-end Templates</li>
      </ul>

      <div class="cta">Get Started
        <svg width="14" height="16" viewBox="0 0 14 16" aria-hidden="true"><polygon points="0,0 14,8 0,16" fill="#0b0b0d"/></svg>
      </div>

      <div class="socials"><span></span><span></span><span></span></div>

      <p class="site-url">https://velmora-frontend.brixwelldev.tech</p>
    </section>

    <svg style="position:absolute;left:0;top:1440px" width="200" height="60" viewBox="0 0 200 60" aria-hidden="true">
      <circle cx="59" cy="31" r="24" fill="var(--like-blue)"/>
      <path d="M50 30 h5 v14 h-5 Z M57 30 l5 -10 a3 3 0 0 1 5 2 l-1 6 h7 a3 3 0 0 1 3 3 l-2 10 a3 3 0 0 1 -3 3 h-14 Z" fill="#fff"/>
      <circle cx="103" cy="31" r="25" fill="var(--alert)" stroke="#fff" stroke-width="2"/>
      <path d="M103 43 l-11 -11 a6.5 6.5 0 0 1 11 -8 a6.5 6.5 0 0 1 11 8 Z" fill="#fff"/>
    </svg>
    <p class="reaction-count">7</p>
    <p class="share-count">3 Shares</p>

    <div class="action-rule"></div>

    <svg style="position:absolute;left:174px;top:1566px" width="54" height="52" viewBox="0 0 54 52" aria-hidden="true">
      <path d="M3 22 h10 v27 h-10 Z M13 24 l9 -19 a5 5 0 0 1 9 3 l-2 11 h15 a5 5 0 0 1 5 6 l-4 19 a5 5 0 0 1 -5 5 h-27" fill="none" stroke="var(--soft-blue)" stroke-width="3.5" stroke-linejoin="round"/>
    </svg>
    <p class="action like">Like</p>

    <svg style="position:absolute;left:672px;top:1566px" width="46" height="52" viewBox="0 0 46 52" aria-hidden="true">
      <g fill="none" stroke="var(--soft-blue)" stroke-width="3.5">
        <circle cx="34" cy="10" r="7"/>
        <circle cx="10" cy="26" r="7"/>
        <circle cx="34" cy="42" r="7"/>
        <line x1="16" y1="22" x2="28" y2="14"/>
        <line x1="16" y1="30" x2="28" y2="38"/>
      </g>
    </svg>
    <p class="action share">Share</p>
  </article>
</div>
</body>
</html>
```